Private Maths Tuition Flyer based in London

I am opening up a new Maths tuition centre in North West London. The flyer will be delivered to over 8,000 homes within the immediate vicinity. The design should be suitable to be printed on an A5 sheet and read in a portrait orientation.

The flyer should include the following:

The headline statement should be "Private Maths Tuition"

Secondary headline statement is the following "GCSE, A-Levels, 11 Plus exams"

Some of service offerings/selling points are:

- Free first session
- Monthly Feedback reports
- Free support outside of sessions
- Clear Target grades
- Personalised Lesson plans
- Tangible Results

Another statement that should be featured is "Book your free session by visiting www.lernova.co.uk" or something similar to that.

"Contact Details:
020 4719 8263
enquiries@lernova.co.uk"

"Address:
Kelbridge Business and Innovation Centre
Ashvale Court
Wrenfield Road
HA4 9QD"

Attached you'll see a logo which should be included and also a map of where we are. I am open to new images for the map if you guys have any, rather than a screen shot from google maps but it should be clear to see.

I would like the content above to be displayed in a clear and concise manner that is easy to read. You have creative license on where this information should be displayed and where the images should be but on the whole it should look aesthetically pleasing on the eye.

Target Market(s)

Students, Parents. Parents who want maths tutors.

Industry/Entity Type

Tutoring

Font styles to use
Sans Serif

Requirements
Must have
• *logo*
• Private Maths Tuition
• GCSE, A-Levels, 11 Plus exams
• - Free first session
• - Monthly Feedback reports
• - Free support outside of sessions
• - Clear Target grades
• - Personalised Lesson plans
• - Tangible Results
• Book your free session by visiting www.lernova.co.uk" or something similar to that.
• Contact Details:
• 020 4719 8263
• enquiries@lernova.co.uk
• Address (*with map*):
• Kelbridge Business and Innovation Centre
• Ashvale Court
• Wrenfield Road
• HA4 9QD
Nice to have
• similar colour scheme as the logo. creative background design.

```html
<!DOCTYPE html>
<html lang="en">
<head>
<meta charset="utf-8">
<title>Private Maths Tuition Flyer</title>
<link rel="stylesheet" href="https://fonts.googleapis.com/css2?family=Cabin+Sketch:wght@400;700&family=Patrick+Hand&family=Open+Sans:wght@400;600;700&display=swap">
<style>
  :root {
    --navy-deep: #0b1d47;
    --navy: #173f86;
    --blue-glow: #4a8be0;
    --chalk: #ffffff;
    --board: #34633a;
    --board-dark: #1f4226;
    --wood: #c07a3a;
    --wood-dark: #8c4f20;
    --footer-bg: #ffffff;
    --footer-line: #d3d8e0;
    --ink: #1c2a4a;
    --ink-soft: #3a4660;
    --brand: #2a9b3c;
    --map: #d7e6cd;
    --map-road: #f4f1e6;
    --pin: #d8453a;
  }
  * { box-sizing: border-box; margin: 0; padding: 0; }
  html, body { width: 847px; height: 1200px; overflow: hidden; background: #fff; }
  .flyer {
    position: relative;
    width: 847px;
    height: 1200px;
    overflow: hidden;
    background: radial-gradient(ellipse 70% 55% at 45% 42%, var(--blue-glow) 0%, var(--navy) 50%, var(--navy-deep) 100%);
  }
  .headline {
    position: absolute;
    top: 20px; left: 0; width: 100%;
    text-align: center;
    font-family: "Cabin Sketch", sans-serif;
    font-weight: 700;
    font-size: 72px;
    line-height: 1.1;
    color: var(--chalk);
  }
  .student-photo {
    position: absolute;
    left: 390px; top: 100px;
    width: 370px; height: 380px;
    background: radial-gradient(ellipse 45% 50% at 50% 55%, rgba(214, 92, 78, 0.75) 0%, rgba(150, 110, 140, 0.55) 45%, rgba(80, 120, 190, 0.25) 75%, rgba(80, 120, 190, 0) 100%);
  }
  .booking {
    position: absolute;
    left: 60px; top: 172px;
    width: 340px;
    font-family: "Patrick Hand", sans-serif;
    font-size: 42px;
    line-height: 1.25;
    color: var(--chalk);
  }
  .chalkboard {
    position: absolute;
    left: 113px; top: 450px;
    width: 607px; height: 467px;
    background: var(--wood);
    border: 3px solid var(--wood-dark);
    padding: 18px;
    box-shadow: 0 12px 26px rgba(0,0,0,0.45);
  }
  .board-surface {
    width: 100%; height: 100%;
    background: radial-gradient(ellipse at 40% 40%, var(--board), var(--board-dark));
    border: 2px solid var(--wood-dark);
    padding: 22px 28px 0 32px;
    font-family: "Patrick Hand", sans-serif;
    color: var(--chalk);
  }
  .exam-levels { font-size: 40px; font-weight: 400; line-height: 1.2; margin-bottom: 10px; }
  .selling-points { list-style: none; font-size: 40px; line-height: 1.13; width: 420px; }
  .still-life {
    position: absolute;
    left: 500px; top: 770px;
    width: 330px; height: 240px;
    background: radial-gradient(ellipse 50% 50% at 50% 50%, rgba(196, 140, 80, 0.9) 0%, rgba(120, 110, 100, 0.7) 50%, rgba(60, 70, 90, 0) 100%);
  }
  .footer {
    position: absolute;
    left: 0; top: 1005px;
    width: 100%; height: 195px;
    background: var(--footer-bg);
    border-top: 2px solid var(--footer-line);
  }
  .location-map {
    position: absolute;
    left: 40px; top: 24px;
    width: 190px; height: 138px;
    background: linear-gradient(135deg, var(--map) 0%, #e9efe2 55%, var(--map-road) 100%);
    border: 1px solid var(--footer-line);
    box-shadow: 0 2px 6px rgba(0,0,0,0.15);
  }
  .map-pin { position: absolute; left: 80px; top: 38px; width: 30px; height: 42px; }
  .contact {
    position: absolute;
    left: 292px; top: 40px;
    font-family: "Open Sans", sans-serif;
    color: var(--ink-soft);
    font-size: 14px;
    line-height: 1.5;
  }
  .contact-label { font-weight: 700; font-size: 17px; color: var(--ink); margin-bottom: 14px; }
  .contact-line { margin-top: 12px; }
  .brand {
    position: absolute;
    right: 32px; top: 96px;
    display: flex; align-items: center; gap: 10px;
    font-family: "Open Sans", sans-serif;
    font-weight: 700;
    font-size: 34px;
    color: var(--brand);
  }
  .brand-square { width: 26px; height: 26px; background: var(--brand); }
</style>
</head>
<body>
<main class="flyer">
  <h1 class="headline">Private Maths Tuition</h1>

  <div class="student-photo" role="img" aria-label="Photo of a young student in glasses holding books"></div>

  <p class="booking">Book your free session by visiting www.lernova.co.uk</p>

  <div class="chalkboard">
    <div class="board-surface">
      <h2 class="exam-levels">GCSE, A-Levels, 11 Plus exams</h2>
      <ul class="selling-points">
        <li>Free first session</li>
        <li>Monthly Feedback reports</li>
        <li>Free support outside of sessions</li>
        <li>Clear Target grades</li>
        <li>Personalised Lesson plans</li>
        <li>Tangible Results</li>
      </ul>
    </div>
  </div>

  <div class="still-life" role="img" aria-label="Stack of books with an apple, ruler and pencils"></div>

  <footer class="footer">
    <div class="location-map" role="img" aria-label="Map showing the tuition centre location">
      <svg class="map-pin" viewBox="0 0 30 42" aria-hidden="true">
        <path d="M15 1C7.3 1 1 7.2 1 14.8 1 25 15 41 15 41s14-16 14-26.2C29 7.2 22.7 1 15 1z" fill="var(--pin)"/>
        <circle cx="15" cy="14.5" r="5.5" fill="#fff"/>
      </svg>
    </div>
    <div class="contact">
      <p class="contact-label">CONTACT :</p>
      <p>Kelbridge Business and Innovation Centre</p>
      <p>Ashvale Court - Wrenfield Road - HA4 9QD</p>
      <p class="contact-line">020 4719 8263 - enquiries@lernova.co.uk</p>
    </div>
    <div class="brand"><span class="brand-square"></span>Lernova</div>
  </footer>
</main>
</body>
</html>
```